Business card for femtech company

Nothing too elaborate but elegant and geared towards the mother and baby market. Prefer full-bleed with logo (attached) rear.

```html
<!DOCTYPE html>
<html lang="en">
<head>
<meta charset="utf-8">
<title>Nestwell – Business Card</title>
<link href="https://fonts.googleapis.com/css2?family=Lato:wght@400;700&display=swap" rel="stylesheet">
<style>
  :root {
    --teal: #5bc4ba;
    --teal-soft: #7dd0c6;
    --grey-text: #8f8f8f;
    --grey-line: #c9c9c9;
    --white: #ffffff;
    --backdrop: #2b2d30;
  }
  * { margin: 0; padding: 0; box-sizing: border-box; }
  html, body {
    width: 1200px; height: 952px; overflow: hidden;
    background: var(--backdrop);
    font-family: "Lato", Arial, sans-serif;
  }
  .canvas {
    position: relative; width: 1200px; height: 952px;
  }
  .card {
    position: absolute; left: 230px;
    width: 740px; height: 423px;
    overflow: hidden;
  }
  /* Front side */
  .card--front { top: 38px; background: var(--white); }
  .front__brand {
    position: absolute; top: 92px; left: 0; width: 100%;
    display: flex; align-items: center; justify-content: center; gap: 22px;
  }
  .brand-dot {
    width: 58px; height: 58px; border-radius: 50%;
    background: var(--teal);
  }
  .brand-name {
    font-weight: 400; font-size: 64px; letter-spacing: 1px;
    color: var(--grey-text); line-height: 1;
  }
  .front__details {
    position: absolute; top: 212px; left: 118px; right: 60px;
    display: flex; gap: 26px;
  }
  .person { text-align: right; padding-top: 2px; }
  .person__name {
    color: var(--teal); font-size: 19px; letter-spacing: 1px;
    text-transform: uppercase; white-space: nowrap;
  }
  .person__name strong { font-weight: 700; }
  .person__role { color: var(--grey-text); font-size: 15px; margin-top: 2px; }
  .contacts { list-style: none; }
  .contacts li {
    display: flex; align-items: center; gap: 10px;
    color: var(--grey-text); font-size: 14px; height: 24px;
  }
  .contact-icon {
    width: 18px; height: 18px; border-radius: 3px;
    background: var(--teal);
    display: flex; align-items: center; justify-content: center;
  }
  .front__rule-thin {
    position: absolute; left: 0; right: 0; top: 320px;
    height: 2px; background: var(--grey-line);
  }
  .front__rule-band {
    position: absolute; left: 0; right: 0; top: 330px;
    height: 9px; background: var(--teal);
  }
  /* Back side */
  .card--back { top: 501px; background: var(--teal); }
  .back__circle {
    position: absolute; left: 60px; top: -60px;
    width: 330px; height: 330px; border-radius: 50%;
    background: var(--teal-soft); opacity: 0.55;
  }
  .back__brand {
    position: absolute; left: 0; right: 0; top: 250px;
    text-align: center;
    color: var(--white); font-weight: 400; font-size: 82px;
    letter-spacing: 2px; line-height: 1;
  }
</style>
</head>
<body>
<main class="canvas">

  <section class="card card--front" aria-label="Business card front">
    <div class="front__brand">
      <span class="brand-dot"></span>
      <span class="brand-name">Nestwell</span>
    </div>

    <div class="front__details">
      <div class="person">
        <p class="person__name">Daniel M. <strong>Hart</strong></p>
        <p class="person__role">Managing Director</p>
      </div>
      <ul class="contacts">
        <li>
          <span class="contact-icon">
            <svg width="12" height="12" viewBox="0 0 24 24"><path fill="#fff" d="M6.6 10.8a15.1 15.1 0 0 0 6.6 6.6l2.2-2.2c.3-.3.7-.4 1-.2 1.1.4 2.3.6 3.6.6.6 0 1 .4 1 1V20c0 .6-.4 1-1 1A17 17 0 0 1 3 4c0-.6.4-1 1-1h3.5c.6 0 1 .4 1 1 0 1.3.2 2.5.6 3.6.1.3 0 .7-.2 1z"/></svg>
          </span>
          +00 987 654 32
        </li>
        <li>
          <span class="contact-icon">
            <svg width="12" height="12" viewBox="0 0 24 24"><rect x="3" y="6" width="18" height="12" fill="none" stroke="#fff" stroke-width="2"/><path d="M3 6l9 7 9-7" fill="none" stroke="#fff" stroke-width="2"/></svg>
          </span>
          hello@nestwell.com
        </li>
        <li>
          <span class="contact-icon">
            <svg width="12" height="12" viewBox="0 0 24 24"><path fill="#fff" d="M6 3l12 8-5 1 3 7-2 1-3-7-5 3z"/></svg>
          </span>
          www.nestwell.com
        </li>
      </ul>
    </div>

    <div class="front__rule-thin"></div>
    <div class="front__rule-band"></div>
  </section>

  <section class="card card--back" aria-label="Business card back">
    <div class="back__circle"></div>
    <p class="back__brand">Nestwell</p>
  </section>

</main>
</body>
</html>
```